Letterhead for Midwest Law Firm

Our law firm does estate planning and trust administration in Wisconsin and Illinois. We recently obtained a new logo and need to incorporate it into new stationary. The stationary needs to list out the attorneys at the firm, but we will want 3 variations, one with three attorneys, one with six, and one with six plus the names of states where each is licensed to practice (possibly as an asterisk with notation somewhere towards bottom of page. As with most traditional law practices, letterhead should be conservative and convey predictability and reliability. We view our brand as being primarily reliability, with prestige as a secondary element. We are upmarket, but would like to avoid seeming pretentious or "slick". We are a smaller firm with a personal touch.

Target Market(s)

Affluent Midwestern Americans approaching at or approaching retirement age.

Industry/Entity Type

Legal

Font styles to use
Serif
Sans Serif

Requirements
Must have
• Must use our logo. Must comply with Brennick Legal Guild Ethics rules: https://www.halvorjudic.org/courts/offices/docs/pqmtnv20annotated.pdf. Must be conventional. Must list names of attorneys and provide contact information for firm. Note that we are asking for three designs with very minor variations. Also, designer must provide letterhead in a format that is industry-standard for stationary printers.
Nice to have
• We would appreciate an alternate version that will look reasonable when printed on a black-and-white printer. Designer can use judgment as to whether to have use grayscale, black/white, or something in between.
Should not have
• No "motto" or "visit our website" extraneous materials. putting the website address somewhere is fine, but overall there is a lot of required text, and we'd like to not appear cluttered.

```html
<!DOCTYPE html>
<html lang="en">
<head>
<meta charset="utf-8">
<title>Halloway &amp; Brandt LLP — Letterhead</title>
<link rel="stylesheet" href="https://fonts.googleapis.com/css2?family=Montserrat:wght@400;500&family=Arimo:wght@400&display=swap">
<style>
  :root {
    --backdrop: #c0c0c0;
    --paper: #ffffff;
    --ink: #111111;
    --ink-strong: #222222;
    --ink-soft: #8a8a8a;
    --ink-body: #9a9a9a;
    --rule: #111111;
  }
  * { box-sizing: border-box; margin: 0; padding: 0; }
  html, body { width: 1200px; height: 1200px; overflow: hidden; background: var(--backdrop); }
  .sheet {
    position: absolute; left: 197px; top: 30px; width: 806px; height: 1140px;
    background: var(--paper);
    font-family: "Montserrat", sans-serif; color: var(--ink);
  }
  .brand {
    position: absolute; left: 53px; top: 60px;
    display: flex; align-items: center; gap: 12px;
  }
  .brand-mark { width: 58px; height: 58px; border-radius: 50%; border: 3px solid var(--ink); }
  .brand-name { font-family: "Montserrat", sans-serif; font-weight: 500; font-size: 20px; color: var(--ink); }
  .contact {
    position: absolute; left: 603px; top: 38px;
    font-family: "Arimo", sans-serif; font-size: 13.5px; line-height: 16px; color: var(--ink);
  }
  .contact-address { margin-bottom: 10px; }
  .contact-line { display: flex; align-items: center; gap: 7px; }
  .contact-line svg { width: 11px; height: 11px; flex: none; }
  .header-rule { position: absolute; left: 53px; top: 140px; width: 701px; height: 1.5px; background: var(--rule); }
  .recipient { position: absolute; left: 83px; top: 258px; }
  .recipient-label { font-size: 14px; font-weight: 500; letter-spacing: 2px; color: var(--ink-strong); margin-bottom: 8px; }
  .recipient-name { font-size: 13px; font-weight: 500; color: var(--ink); margin-bottom: 6px; }
  .recipient-detail { font-size: 11px; line-height: 18px; color: var(--ink-soft); }
  .letter-date { position: absolute; right: 81px; top: 259px; font-size: 11.5px; color: var(--ink-soft); }
  .letter-body {
    position: absolute; left: 83px; top: 412px; width: 643px;
    font-size: 11.3px; line-height: 14.3px; color: var(--ink-body); text-align: justify;
  }
  .letter-body p { margin-bottom: 14.3px; }
  .signature-area {
    position: absolute; left: 83px; top: 806px; width: 140px; height: 32px;
    background: linear-gradient(90deg, #f1f1f1, #e6e6e6);
  }
  .signatory { position: absolute; left: 81px; top: 852px; }
  .signatory-name { font-size: 12.5px; font-weight: 500; color: var(--ink-strong); }
  .signatory-title { font-size: 10.5px; color: var(--ink-soft); margin-top: 2px; }
</style>
</head>
<body>
<main class="sheet">
  <header>
    <div class="brand">
      <span class="brand-mark"></span>
      <span class="brand-name">Halloway &amp; Brandt LLP</span>
    </div>
    <address class="contact" style="font-style:normal">
      <div class="contact-address">Your address, city<br>state, ZIP 0000</div>
      <div class="contact-line">
        <svg viewBox="0 0 24 24"><path fill="#111" d="M6.6 10.8a15 15 0 0 0 6.6 6.6l2.2-2.2c.3-.3.7-.4 1-.2 1.1.4 2.3.6 3.6.6.6 0 1 .4 1 1V20c0 .6-.4 1-1 1A17 17 0 0 1 3 4c0-.6.4-1 1-1h3.5c.6 0 1 .4 1 1 0 1.3.2 2.5.6 3.6.1.3 0 .7-.2 1z"/></svg>
        <span>123-555-0142</span>
      </div>
      <div class="contact-line">
        <svg viewBox="0 0 24 24"><path fill="#111" d="M2 5h20v14H2z"/><path fill="none" stroke="#fff" stroke-width="2" d="M2 6l10 7 10-7"/></svg>
        <span>info@hallowaybrandt.com</span>
      </div>
      <div class="contact-line">
        <svg viewBox="0 0 24 24"><circle cx="12" cy="12" r="10" fill="#111"/><path fill="none" stroke="#fff" stroke-width="1.6" d="M2 12h20M12 2c3 3 3 17 0 20M12 2c-3 3-3 17 0 20"/></svg>
        <span>www.hallowaybrandt.com</span>
      </div>
    </address>
    <div class="header-rule"></div>
  </header>

  <section class="recipient">
    <div class="recipient-label">TO</div>
    <div class="recipient-name">Daniel Ostrander</div>
    <div class="recipient-detail">Human Resources<br>Northfield Systems Inc.<br>1105-D Larkspur Lane, Fairhaven<br>E89 USA</div>
  </section>
  <div class="letter-date">Friday, 01/01/2018</div>

  <article class="letter-body">
    <p>Lorem ipsum dolor sit amet, consectetuer adipiscing elit, sed diam nonmmy nibh euismod tincidunt ut laoreet dolore magna aliquam erat volutpat. Ut wisi enim ad minim veniam, quis nostrud exerci tationmcorper suscipit lobortis nisl ut aliquip ex ea commodo consequat. Duis autem vel eum iriure dolor in hendrerit in vulputate velit esse molestie consequat, vel illum dolore eu feugiat nulla facilisis at vero eros et accumsan et iusto odio dignissim qui blandit praesent luptatum zzril delenit augue duis dolore te feugait nulla facilisi.</p>
    <p>Nam liber tempor cum soluta nobis eleifend option congue nihil imprdiet doming id quod mazim placerat facer possim assum. Typi non habent claritatem insitam;</p>
    <p>Est usus legentis in iis qui facit eorum claritatem.</p>
    <p>Investigationes demonstraverunt lectores legere me lius quod ii legunt saepius. Claritas est etiam processus dynamicus, qui sequitur mutationem consuetudium lectorum. Mirum est notare quam littera gothica, quam nunc putamus parum claram, anteposuerit litterarum formas humanitatis per seacula quarta decima et quinta decima. Eodem modo typi, qui nunc nobis videntur parum clari, fiant sollemnes in futurum.</p>
    <p>consectetuer adipiscing elit, sed diam nonummy nibh euismod tincidunt ut laoreet dolore magna aliquam erat volutpat. Ut wisi enim ad minim veniam, quis nostrud exerci tation ullamcorper suscipit lobortis nisl ut aliquip ex ea commodo consequat. Duis autem vel eum iriure dolor in hendrerit in vulputate velit esse molestie consequat, vel illum dolore eu feugiat nulla facilisis at vero eros et accumsan et iusto odio dignissim qui blandit praesent luptatum zzril delenit augue duis dolore te feugait nulla facilisi.</p>
    <p>Nam liber tempor cum soluta nobis eleifend option congue nihil imperdiet .</p>
  </article>

  <div class="signature-area" role="img" aria-label="Handwritten signature of Peter Lindqvist"></div>
  <footer class="signatory">
    <div class="signatory-name">Peter Lindqvist</div>
    <div class="signatory-title">Managing Director</div>
  </footer>
</main>
</body>
</html>
```